Harbor Scholars Collective
Bus Cards, Stationery
Harbor Scholars Collective - Education
Creative Brief
Modern
Dr. Maribel Ostrander
President
4870 North Welbrook Avenue, Suite 316 Larkhaven, Marivale 33427
xxx xxx xxxx
mostrander@brightquill.example
brightquill.example
Please be creative with card size dimensions as long as they fit within a standard 3 1/2 x 2 (i.e. 2 x 2, or 3 x 2). I have entered x's in areas where I still do not have the information. My phone lines have not been connected yet. I will have printer replace x's with actual numbers once I know them.
School Readiness Tutoring - All Subjects High School Entrance Exams SAT/ACT Prep College Transition Private and Group Classes Available (in smaller font)

```html
<!DOCTYPE html>
<html lang="en">
<head>
<meta charset="utf-8">
<title>Harbor Scholars Collective – Business Card</title>
<link rel="stylesheet" href="https://fonts.googleapis.com/css2?family=Tinos:wght@400;700&display=swap">
<style>
  :root {
    --page-bg: #e9e7e4;
    --card-white: #ffffff;
    --navy: #1d3f86;
    --blue-deep: #173e8c;
    --blue-bright: #1f8fd1;
    --text-grey: #6b6e73;
    --brand-blue: #2a7fc9;
    --on-blue: #ffffff;
  }
  * { margin: 0; padding: 0; box-sizing: border-box; }
  html, body { width: 1200px; height: 965px; overflow: hidden; }
  body {
    background: var(--page-bg);
    font-family: "Tinos", "Times New Roman", serif;
    position: relative;
  }
  .card {
    position: absolute;
    left: 100px; top: 197px;
    width: 1000px; height: 571px;
    border-radius: 40px;
    overflow: hidden;
    background: var(--card-white);
    box-shadow: 0 10px 30px rgba(0,0,0,.18);
  }
  .card-waves { position: absolute; inset: 0; }
  .brand {
    position: absolute;
    left: 145px; top: 60px;
    width: 300px;
    text-align: center;
  }
  .brand-mark {
    display: block;
    width: 130px; height: 130px;
    margin: 0 auto 18px;
    border-radius: 50%;
    background: var(--brand-blue);
  }
  .brand-name {
    color: var(--text-grey);
    font-size: 25px;
    line-height: 1.2;
    letter-spacing: 1px;
    text-transform: uppercase;
  }
  .person { position: absolute; left: 542px; top: 100px; }
  .person-name { color: var(--navy); font-size: 36px; font-weight: 700; }
  .person-title { color: var(--text-grey); font-size: 27px; margin-top: 10px; }
  .address {
    position: absolute;
    right: 480px; top: 374px;
    text-align: right;
    color: var(--on-blue);
    font-size: 26px;
    font-style: normal;
    line-height: 38px;
  }
  .divider {
    position: absolute;
    left: 527px; top: 376px;
    width: 2px; height: 150px;
    background: var(--on-blue);
  }
  .contacts {
    position: absolute;
    left: 540px; top: 374px;
    list-style: none;
    color: var(--on-blue);
    font-size: 25px;
    line-height: 38px;
  }
  .contacts li { display: flex; align-items: center; gap: 10px; }
  .contacts svg { width: 22px; height: 22px; flex: none; }
</style>
</head>
<body>
  <article class="card">
    <svg class="card-waves" viewBox="0 0 1000 571" preserveAspectRatio="none" aria-hidden="true">
      <defs>
        <linearGradient id="blueBand" x1="0" y1="0" x2="1" y2="0">
          <stop offset="0" stop-color="#173e8c"/>
          <stop offset="0.55" stop-color="#1f8fd1"/>
          <stop offset="1" stop-color="#173e8c"/>
        </linearGradient>
        <linearGradient id="greySwoosh" x1="0" y1="0" x2="1" y2="0">
          <stop offset="0" stop-color="#9ea2a8"/>
          <stop offset="1" stop-color="#e4e5e8"/>
        </linearGradient>
      </defs>
      <path d="M0,345 C180,290 380,290 560,312 C760,336 880,300 1000,270 L1000,300 C880,320 760,350 560,330 C380,312 200,320 0,372 Z" fill="url(#greySwoosh)"/>
      <path d="M0,372 C200,320 380,312 560,330 C760,350 880,320 1000,300 L1000,571 L0,571 Z" fill="url(#blueBand)"/>
    </svg>

    <div class="brand">
      <span class="brand-mark"></span>
      <p class="brand-name">Harbor Scholars<br>Collective</p>
    </div>

    <div class="person">
      <h1 class="person-name">Dr. Maribel Ostrander</h1>
      <p class="person-title">President</p>
    </div>

    <address class="address">
      4870 North Welbrook Avenue,<br>Suite 316<br>Larkhaven,<br>Marivale 33427
    </address>

    <div class="divider"></div>

    <ul class="contacts">
      <li>
        <svg viewBox="0 0 24 24" fill="#fff"><path d="M6.6 10.8a15 15 0 0 0 6.6 6.6l2.2-2.2a1 1 0 0 1 1-.25 11.4 11.4 0 0 0 3.6.6 1 1 0 0 1 1 1V20a1 1 0 0 1-1 1A17 17 0 0 1 3 4a1 1 0 0 1 1-1h3.5a1 1 0 0 1 1 1c0 1.25.2 2.45.6 3.6a1 1 0 0 1-.25 1z"/></svg>
        xxx xxx xxxx
      </li>
      <li>
        <svg viewBox="0 0 24 24" fill="#fff"><rect x="6" y="2" width="12" height="7"/><rect x="2" y="10" width="20" height="12" rx="2"/><rect x="6" y="14" width="12" height="2" fill="#1f6fb8"/></svg>
        xxx xxx xxxx
      </li>
      <li>
        <svg viewBox="0 0 24 24" fill="none" stroke="#fff" stroke-width="2.4"><circle cx="12" cy="12" r="4"/><path d="M16 8v5.5a2.5 2.5 0 0 0 5 0V12a9 9 0 1 0-3.5 7.1"/></svg>
        mostrander@brightquill.example
      </li>
      <li>
        <svg viewBox="0 0 24 24" fill="none" stroke="#fff" stroke-width="2"><circle cx="12" cy="12" r="9.5"/><ellipse cx="12" cy="12" rx="4" ry="9.5"/><path d="M2.5 12h19M4 7h16M4 17h16"/></svg>
        brightquill.example
      </li>
    </ul>
  </article>
</body>
</html>
```